Exciting Wordpress Project: New Consulting Firm

A wordpress design is needed for my new consulting company, Verbrook Partners.

The site should have a modern feel to it and use the colour scheme from the attached 3 vector files.

I only know a little about Wordpress but the site should be mobile friendly.

The following menu options should be created:
1. Home
2. Verbrook service lines (with sub-menus)
3. Our people
4. Verbrook case studies
5. The Verbrook story
6. Contact Verbrook
Updates

Reason: Allow just one or two more designs to come in before deciding.

Target Market(s)

Government departments and medium private sector organisations

Industry/Entity Type

It Company

Requirements
Must have
• 1. Inclue Verbrook logo at top of each page
2. Slider on the home page
3. Global navigation
4. Drop down navigation
5. Social media links
6. Search and contact details at the top of the home page
7. Home page to fit on one screen
8. Terms & Conditions, Privacy Policy at the bottom of the home page
9. Newsletter (i.e. postwren) subscription on home page
Nice to have
• 1. Background watermark from the Verbrook logo
2. A layout similar to the photo attached - however open to different ideas

```html
<!DOCTYPE html>
<html lang="en">
<head>
<meta charset="utf-8">
<title>Verbrook Partners</title>
<link href="https://fonts.googleapis.com/css2?family=Source+Sans+3:ital,wght@0,400;0,600;0,700;1,400;1,600&display=swap" rel="stylesheet">
<style>
:root{
  --blue:#0b3d9c;
  --blue-dark:#062d7a;
  --blue-text:#0a3a96;
  --gray-text:#4a4a4c;
  --body-text:#555;
  --logo-gray:#6b6b6d;
  --panel-gray:#6f6f71;
  --button-dark:#4a4a4a;
  --line:#cfcfcf;
  --white:#fff;
}
*{box-sizing:border-box;margin:0;padding:0}
html,body{width:1200px;height:954px;overflow:hidden;background:var(--white)}
body{position:relative;font-family:"Source Sans 3",sans-serif;color:var(--gray-text)}
.abs{position:absolute}

.brand-watermark{left:150px;top:500px;font-size:170px;font-weight:700;color:#000;opacity:.045;letter-spacing:18px;white-space:nowrap;line-height:1}

.logo{left:130px;top:38px;width:230px}
.logo-name{font-size:40px;font-weight:600;color:var(--logo-gray);letter-spacing:1px;line-height:1}
.logo-sub{font-size:14px;font-weight:600;color:var(--logo-gray);letter-spacing:10.5px;margin-top:6px;line-height:1}

.call{right:130px;top:36px;display:flex;align-items:center;gap:8px;white-space:nowrap}
.call-label{font-size:18px;font-weight:600;color:var(--blue-text)}
.call-number{font-size:24px;font-weight:600;color:var(--gray-text)}

.search{left:849px;top:76px;width:222px;height:26px;border:1px solid #c9c9c9;border-radius:6px;background:linear-gradient(#f7f7f7,#ececec);padding:0 12px;display:flex;align-items:center;justify-content:space-between}
.search-placeholder{font-size:12px;font-style:italic;color:#999}

.main-nav{left:130px;top:124px;width:940px;height:46px;background:linear-gradient(#0d47b0,var(--blue-dark));border-radius:4px;display:flex;align-items:center;justify-content:space-between;padding:0 17px 0 18px}
.main-nav a{color:var(--white);text-decoration:none;font-size:15px;letter-spacing:.3px}
.main-nav .sep{color:#c8d4ef;font-size:15px}

.slider{left:130px;top:182px;width:700px;height:335px;border:1px solid #bbb;border-radius:3px;overflow:hidden;background:linear-gradient(100deg,#cdd6dc 0%,#e6d1bc 25%,#d9b895 45%,#e3cbb2 65%,#c9b6a3 85%,#b7aca4 100%)}
.slide-caption{left:252px;top:223px;width:447px;height:73px;background:rgba(255,255,255,.78);padding:7px 15px}
.slide-title{font-size:20px;font-weight:600;font-style:italic;color:var(--blue-dark);line-height:1.1}
.slide-text{font-size:14px;color:#333;line-height:18px;margin-top:4px}
.slide-dots{left:15px;top:302px;display:flex;gap:5px}
.slide-dots span{width:15px;height:15px;border-radius:3px;background:#eee}
.slide-dots span.active{background:var(--blue)}

.newsletter{left:850px;top:182px;width:220px;height:335px;background:var(--panel-gray);border:1px solid #999;border-radius:3px;padding:16px 16px;color:var(--white)}
.newsletter-title{font-size:20px;font-weight:700;line-height:1}
.newsletter-sub{font-size:18px;line-height:1;margin-top:4px}
.newsletter-text{font-size:12.5px;line-height:15.5px;margin-top:9px}
.field{position:absolute;left:16px;width:185px;height:37px;background:var(--white);border:1px solid #ddd;border-radius:4px;font-size:13px;color:#999;padding:10px 15px}
.btn{position:absolute;height:28px;border-radius:3px;color:var(--white);font-size:13px;display:flex;align-items:center;justify-content:center}
.btn-blue{background:linear-gradient(#1150bf,var(--blue-dark));width:97px}
.btn-dark{background:linear-gradient(#616161,#3c3c3c);width:97px}

.welcome-title{left:131px;top:546px;font-size:24px;color:var(--gray-text);font-weight:400}
.welcome-title b{color:var(--blue-text);font-weight:400}
.welcome-text{left:131px;top:586px;width:458px;font-size:13.5px;line-height:23px;color:var(--body-text)}

.tab{top:552px;width:169px;height:36px;font-size:16px;display:flex;align-items:center;justify-content:center;border-radius:3px 3px 0 0}
.tab-active{left:610px;background:linear-gradient(#0d47b0,var(--blue-dark));color:var(--white)}
.tab-idle{left:780px;background:linear-gradient(#e6e6e6,#cfcfcf);color:#555}
.pager{left:1019px;top:558px;display:flex;gap:8px}

.case-box{left:609px;top:588px;width:462px;height:215px;border:1px solid var(--line);border-radius:4px;background:linear-gradient(#fff,#f6f6f6)}
.case-photo{left:15px;top:21px;width:123px;height:115px;border:1px solid #bbb;background:linear-gradient(135deg,#d8dbe0,#b9a896 50%,#8e8f95)}
.case-title{left:156px;top:17px;width:290px;font-size:15.5px;line-height:20px;color:var(--blue-text)}
.case-text{left:156px;top:62px;width:295px;font-size:13px;line-height:20px;color:var(--body-text)}

.footer{left:0;top:826px;width:1200px;height:128px;border-top:1px solid #ddd;background:linear-gradient(#f0f0f0,#fff 60%)}
.footer-links{left:132px;top:35px;font-size:13.5px;color:#555;white-space:nowrap}
.footer-links span.sep{margin:0 7px}
.copyright{left:132px;top:66px;font-size:13.5px;color:#555;white-space:nowrap}
.copyright b{color:var(--blue-text);font-weight:600}
.copyright span.sep{margin:0 7px}
.social{left:921px;top:38px;display:flex;gap:10px}
.social span{width:30px;height:30px;border-radius:4px}
</style>
</head>
<body>

<div class="abs brand-watermark" aria-hidden="true">VERBROOK</div>

<header>
  <div class="abs logo">
    <div class="logo-name">VERBROOK</div>
    <div class="logo-sub">PARTNERS</div>
  </div>

  <div class="abs call">
    <svg width="22" height="16" viewBox="0 0 22 16" aria-hidden="true"><path d="M2 5 Q11 -1 20 5 L18 8 L15 6 V4 H7 V6 L4 8 Z" fill="#444"/><rect x="4" y="8" width="14" height="7" rx="2" fill="#444"/><circle cx="11" cy="11.5" r="2" fill="#fff"/></svg>
    <span class="call-label">Call Us:</span>
    <span class="call-number">12 555 0190</span>
  </div>

  <div class="abs search">
    <span class="search-placeholder">Search...</span>
    <svg width="20" height="18" viewBox="0 0 20 18" aria-hidden="true"><circle cx="7.5" cy="7" r="5.5" fill="none" stroke="#163f8f" stroke-width="2.5"/><line x1="11.5" y1="11" x2="18" y2="16" stroke="#163f8f" stroke-width="3.5" stroke-linecap="round"/></svg>
  </div>

  <nav class="abs main-nav">
    <a href="#">Home</a><span class="sep">|</span>
    <a href="#">Verbrook Service Lines</a><span class="sep">|</span>
    <a href="#">Our People</a><span class="sep">|</span>
    <a href="#">Verbrook Case Studies</a><span class="sep">|</span>
    <a href="#">The Verbrook Story</a><span class="sep">|</span>
    <a href="#">Contact Verbrook</a>
  </nav>
</header>

<section class="abs slider" role="img" aria-label="Photo of a smiling team of four consultants">
  <div class="abs slide-caption">
    <div class="slide-title">Nam fermentum vestibulum purus id aliquet.</div>
    <div class="slide-text">Vestibulum ante ipsum primis in faucibus orci luctus<br>et ultrices</div>
  </div>
  <div class="abs slide-dots"><span class="active"></span><span></span><span></span><span></span></div>
</section>

<aside class="abs newsletter">
  <div class="newsletter-title">Newsletter</div>
  <div class="newsletter-sub">Subscribe</div>
  <p class="newsletter-text">Nunc dignissim lectus vitae eros placerat euismod. Aenean lacinia sodales eros, sit amet molestie enim consectetur eget.</p>
  <div class="field" style="top:169px">Enter Name</div>
  <div class="field" style="top:221px">Enter Email</div>
  <div class="btn btn-blue" style="left:100px;top:282px">Read More</div>
</aside>

<main>
  <h1 class="abs welcome-title">Welcome to <b>Verbrook Partners</b></h1>
  <p class="abs welcome-text">Aliquam molestie, mi et imperdiet euismod, dui purus auctor tellus, et interdum lacus lectus et ante. Sed accumsan sollicitudin sapien, sit amet adipiscing turpis gravida ac. In congue, neque ac lobortis volutpat, libero mauris varius mi, vitae suscipit ipsum ligula vitae risus. Duis aliquam nibh a dui iaculis viverra id a velit. Vivamus egestas risus in magna varius commodo. Sed semper viverra egestas. Etiam pretium porttitor lectus, vel ornare neque porta volutpat.</p>
  <div class="btn btn-dark" style="left:133px;top:774px">Read More</div>

  <div class="abs tab tab-active">Verbrook Case Studies</div>
  <div class="abs tab tab-idle">The Verbrook Story</div>
  <div class="abs pager" aria-hidden="true">
    <svg width="23" height="23" viewBox="0 0 23 23"><circle cx="11.5" cy="11.5" r="10.5" fill="#eee" stroke="#aaa"/><path d="M14 7 L8 11.5 L14 16 Z" fill="#222"/></svg>
    <svg width="23" height="23" viewBox="0 0 23 23"><circle cx="11.5" cy="11.5" r="10.5" fill="#eee" stroke="#aaa"/><path d="M9 7 L15 11.5 L9 16 Z" fill="#222"/></svg>
  </div>

  <article class="abs case-box">
    <div class="abs case-photo" role="img" aria-label="Photo of three colleagues looking at a laptop"></div>
    <div class="abs case-title">Aliquam ullamcorper tempor felis, nec condimentum odio aliquet vitae.</div>
    <p class="abs case-text">Vestibulum vel metus sit amet turpis bibendum tincidunt vel sit amet quam. Pellentesque habitant morbi tristique senectus et netus et malesuada fames ac turpis egestas.</p>
    <div class="btn btn-dark" style="left:348px;top:167px">Read More</div>
  </article>
</main>

<footer class="abs footer">
  <div class="abs footer-links">Home<span class="sep">|</span> Verbrook Service Lines <span class="sep">|</span> Our People <span class="sep">|</span>Verbrook Case Studies <span class="sep">|</span>The Verbrook Story <span class="sep">|</span>Contact Verbrook</div>
  <div class="abs copyright">Copyright © 2013 <b>Verbrook</b>. All Right Reserved <span class="sep">|</span>T&amp;Cs <span class="sep">|</span> Privacy Policy</div>
  <div class="abs social" aria-label="Social media links">
    <span style="background:#3b5ea8"></span>
    <span style="background:#1f7ab8"></span>
    <span style="background:#4fc1e3"></span>
    <span style="background:#f28a1e"></span>
  </div>
</footer>

</body>
</html>
```